Biz Cards for Lumivale Associates

Lumivale Associates is seeking a single-sided business card that is more visually-appealing than our current design (see attached).

Notes:
- Our colors are blue & teal.
- Our tag line must be large enough to be easily read
- We don't necessarily need our address included (that's just the biz office)
- We'd like to add our email address: Lumivale512@brindlemail.net

Thanks!

Industry/Entity Type

Business

Contact Information for Business Card

Standard size
PSD file required w/ text on its own layer

Colors
86cfc6
3277b5

```html
<!DOCTYPE html>
<html lang="en">
<head>
<meta charset="utf-8">
<title>Lumivale Associates – Business Card</title>
<link rel="stylesheet" href="https://fonts.googleapis.com/css2?family=Montserrat:wght@400;500;600;700&family=Lato:ital,wght@1,400&display=swap">
<style>
  :root {
    --blue: #3277b5;
    --blue-deep: #2f86c0;
    --teal: #86cfc6;
    --teal-bright: #5fc8cc;
    --ink: #3a3a3a;
    --paper: #ffffff;
    --stage: #1b1b1d;
  }
  * { margin: 0; padding: 0; box-sizing: border-box; }
  html, body { width: 1200px; height: 894px; overflow: hidden; background: var(--stage); }
  .canvas { position: relative; width: 1200px; height: 894px; }
  .card {
    position: absolute; left: 100px; top: 161px; width: 1000px; height: 572px;
    background: var(--paper); border-radius: 22px; overflow: hidden;
    font-family: "Montserrat", sans-serif; color: var(--ink);
  }
  .card-swooshes { position: absolute; inset: 0; }
  .brand { position: absolute; left: 200px; top: 100px; display: flex; align-items: center; gap: 28px; }
  .brand-dot { width: 140px; height: 140px; border-radius: 50%; border: 3px solid var(--ink); flex: none; }
  .brand-name { font-family: "Montserrat", sans-serif; font-weight: 600; font-size: 46px; line-height: 1.1; color: var(--ink); letter-spacing: 1px; }
  .tagline {
    position: absolute; left: 368px; top: 222px;
    font-family: "Lato", sans-serif; font-style: italic; font-size: 18px; color: var(--blue);
  }
  .person { position: absolute; right: 560px; top: 352px; text-align: right; }
  .person-name { font-size: 28px; font-weight: 700; color: var(--blue); }
  .person-name .surname { color: var(--teal-bright); }
  .person-role { font-size: 19px; font-weight: 600; color: var(--blue); margin-top: 10px; }
  .person-address { font-size: 19px; line-height: 1.6; margin-top: 8px; }
  .divider { position: absolute; left: 460px; top: 362px; width: 2px; height: 140px; background: var(--blue); }
  .contacts { position: absolute; left: 492px; top: 362px; list-style: none; }
  .contacts li { display: flex; align-items: center; gap: 18px; font-size: 20px; height: 36px; }
  .contacts svg { width: 18px; height: 18px; fill: var(--blue); flex: none; }
</style>
</head>
<body>
<div class="canvas">
  <div class="card">
    <svg class="card-swooshes" viewBox="0 0 1000 572" aria-hidden="true">
      <path d="M700 0 C860 20 960 140 1000 300 L1000 0 Z" fill="var(--teal-bright)"/>
      <path d="M745 0 C880 35 975 150 1000 275 L1000 0 Z" fill="var(--blue-deep)"/>
      <path d="M0 330 C20 440 110 530 230 572 L0 572 Z" fill="var(--blue)"/>
      <path d="M0 355 C25 455 100 530 200 572 L0 572 Z" fill="var(--teal)"/>
    </svg>

    <div class="brand">
      <div class="brand-dot"></div>
      <div class="brand-name">Lumivale<br>Associates Ltd</div>
    </div>
    <p class="tagline">Thoughtful Care. Steady Support. Brighter Days.</p>

    <div class="person">
      <p class="person-name">Maren <span class="surname">Holloway,RN</span></p>
      <p class="person-role">Mental Health Therapist</p>
      <p class="person-address">4120 Alder Ridge Rd Suite 310<br>Fairbrook, OH&nbsp; 44210</p>
    </div>

    <div class="divider"></div>

    <ul class="contacts">
      <li><svg viewBox="0 0 24 24"><path d="M6.6 10.8a15 15 0 0 0 6.6 6.6l2.2-2.2c.3-.3.7-.4 1-.2 1.1.4 2.3.6 3.6.6.6 0 1 .4 1 1V20c0 .6-.4 1-1 1A17 17 0 0 1 3 4c0-.6.4-1 1-1h3.5c.6 0 1 .4 1 1 0 1.3.2 2.5.6 3.6.1.3 0 .7-.2 1z"/></svg>(855) 555-0142</li>
      <li><svg viewBox="0 0 24 24"><path d="M6 3h12v5H6zM4 9h16a2 2 0 0 1 2 2v6h-4v4H6v-4H2v-6a2 2 0 0 1 2-2zm4 7v3h8v-3z"/></svg>(330) 555-0187</li>
      <li><svg viewBox="0 0 24 24"><path d="M2 5h20v2l-10 6L2 7zM2 9l10 6 10-6v10H2z"/></svg>Lumivale512@brindlemail.net</li>
      <li><svg viewBox="0 0 24 24"><path d="M12 2a10 10 0 1 0 0 20 10 10 0 0 0 0-20zm6.9 9h-3a15 15 0 0 0-1.3-5.6A8 8 0 0 1 18.9 11zM12 4.1c.9 1.2 1.8 3.6 1.9 6.9h-3.8c.1-3.3 1-5.7 1.9-6.9zM9.4 5.4A15 15 0 0 0 8.1 11h-3a8 8 0 0 1 4.3-5.6zM5.1 13h3a15 15 0 0 0 1.3 5.6A8 8 0 0 1 5.1 13zm6.9 6.9c-.9-1.2-1.8-3.6-1.9-6.9h3.8c-.1 3.3-1 5.7-1.9 6.9zm2.6-1.3a15 15 0 0 0 1.3-5.6h3a8 8 0 0 1-4.3 5.6z"/></svg>www.Lumivale.net</li>
    </ul>
  </div>
</div>
</body>
</html>
```